Vacation giveaway landing page design

We are giving away a holiday/vacation to Rome and we need a landing page designed that will entice people to enter their email address for a chance to win!

Full brief, examples and everything else can be found in this document: https://files.quorvanshare.net/page/7-tmzrwpQY4vxkaLn8sbgeXu2fcTo5kWdn3jhpyuBc29m/open?mode=viewing

Number of Pages Required

1 page

```html
<!DOCTYPE html>
<html lang="en">
<head>
<meta charset="utf-8">
<title>Wanderlot – Win a trip to Rome</title>
<link rel="stylesheet" href="https://fonts.googleapis.com/css2?family=Fira+Sans+Extra+Condensed:wght@400;600;700&family=Playfair+Display:ital,wght@1,900&family=Roboto+Condensed:wght@400;700&family=Mulish:ital,wght@1,600&display=swap">
<style>
:root{
  --teal:#41c0b6;
  --teal-dark:#2fa79d;
  --red:#f2403d;
  --gold:#f5b72e;
  --ink:#2b2b2b;
  --grey:#555;
  --field:#ececec;
  --quote:#d5d5d5;
  --white:#fff;
}
*{box-sizing:border-box;margin:0;padding:0}
html,body{width:1200px;height:1110px;overflow:hidden;background:var(--white)}
body{position:relative;font-family:"Roboto Condensed",sans-serif;color:var(--ink)}
.screen{position:absolute;background:var(--white);box-shadow:0 12px 30px rgba(0,0,0,.22);overflow:hidden}
.screen--desktop{left:14px;top:14px;width:799px;height:919px}
.screen--mobile{left:848px;top:14px;width:326px;height:1040px}
.hero{position:relative;width:100%;background:linear-gradient(100deg,#5f7d55 0%,#9cc6b4 22%,#b9d8c8 42%,#c8b89a 60%,#9b8a6f 80%,#6f6a55 100%)}
.screen--desktop .hero{height:441px}
.screen--mobile .hero{height:484px}
.hero__photo{position:absolute;inset:0}
.brand{position:absolute;left:0;right:0;display:flex;align-items:center;justify-content:center;gap:5px;font-family:"Fira Sans Extra Condensed",sans-serif;font-weight:700;color:#1a1a1a;letter-spacing:.5px}
.brand__dot{width:14px;height:14px;border-radius:50%;background:#1a1a1a}
.headline{position:absolute;left:0;right:0;text-align:center}
.headline__lead{display:block;font-family:"Fira Sans Extra Condensed",sans-serif;font-weight:700;color:var(--teal)}
.headline__city{display:block;font-family:"Playfair Display",serif;font-style:italic;font-weight:900;color:var(--white);line-height:.85;letter-spacing:-2px}
.headline__offer{display:block;font-family:"Fira Sans Extra Condensed",sans-serif;color:var(--white);text-shadow:0 1px 3px rgba(0,0,0,.35)}
.stars{color:var(--gold)}
.signup{position:absolute;background:var(--white)}
.signup__field{background:var(--field);color:#8a8a8a;font-family:"Fira Sans Extra Condensed",sans-serif;display:flex;align-items:center}
.signup__button{background:var(--red);color:var(--white);font-family:"Fira Sans Extra Condensed",sans-serif;font-weight:700;display:flex;align-items:center;justify-content:center}
.legal{position:absolute;text-align:center;color:var(--white);font-family:"Roboto Condensed",sans-serif}
.legal u{text-decoration:underline}
.quote-badge{position:absolute;border-radius:50%;background:var(--teal);border:2px solid var(--white);display:flex;align-items:center;justify-content:center;color:var(--white);font-family:"Playfair Display",serif;font-weight:900;font-style:italic;z-index:2}
.section-title{position:absolute;left:0;right:0;text-align:center;font-family:"Fira Sans Extra Condensed",sans-serif;color:var(--ink)}
.card{position:absolute;background:var(--white);border-top:2px solid var(--teal);box-shadow:0 1px 5px rgba(0,0,0,.16);text-align:center}
.card__avatar{position:absolute;left:50%;transform:translateX(-50%);border-radius:50%;background:radial-gradient(circle at 50% 40%,#c99b7c,#6b4634 75%);border:2px solid var(--white)}
.card__title{font-family:"Fira Sans Extra Condensed",sans-serif;font-weight:600;color:var(--ink)}
.card__title em{font-style:normal;color:var(--gold)}
.card__mark{font-family:"Playfair Display",serif;font-weight:900;color:var(--quote);line-height:1}
.card__text{font-family:"Mulish",sans-serif;font-style:italic;font-weight:600;color:var(--grey)}
.dots{position:absolute;left:0;right:0;display:flex;justify-content:center;align-items:center}
.dots span{border-radius:50%;border:1px solid #888}
.dots span.is-active{background:#888}
.footer{position:absolute;left:0;right:0;bottom:0;background:var(--teal);color:var(--white);text-align:center}
.footer__links a{display:block;color:var(--white);text-decoration:none;font-family:"Fira Sans Extra Condensed",sans-serif;font-weight:700}
.payments{display:flex;justify-content:center}
.payments span{background:#f4f4f4;border:1px solid #777;border-radius:2px}
.footer__small{font-family:"Roboto Condensed",sans-serif}

/* desktop */
.screen--desktop .brand{top:17px;font-size:14px}
.screen--desktop .headline{top:82px}
.screen--desktop .headline__lead{font-size:32px;line-height:1}
.screen--desktop .headline__city{font-size:98px;margin-top:-4px}
.screen--desktop .headline__offer{font-size:20px;margin-left:60px}
.screen--desktop .signup{left:233px;top:247px;width:334px;height:34px;display:flex;gap:8px;padding:5px 9px}
.screen--desktop .signup__field{flex:1;font-size:8px;padding-left:11px}
.screen--desktop .signup__button{flex:1;font-size:8px}
.screen--desktop .legal{left:230px;width:340px;top:293px;font-size:6px;line-height:1.35}
.screen--desktop .quote-badge{left:384px;top:425px;width:33px;height:33px;font-size:24px}
.screen--desktop .section-title{top:484px;font-size:19px}
.screen--desktop .card{top:560px;width:187px;height:167px;padding:52px 14px 0}
.screen--desktop .card__avatar{top:-26px;width:56px;height:56px}
.screen--desktop .card__title{font-size:6.3px}
.screen--desktop .card__mark{font-size:30px;margin:4px 0 -6px}
.screen--desktop .card__text{font-size:8.4px;line-height:1.8}
.screen--desktop .dots{top:747px;gap:5px}
.screen--desktop .dots span{width:5px;height:5px}
.screen--desktop .dots span.is-active{width:7px;height:7px}
.screen--desktop .footer{height:144px;padding-top:17px}
.screen--desktop .footer__links a{font-size:8.5px;line-height:15px}
.screen--desktop .payments{gap:3px;margin:9px 0 11px}
.screen--desktop .payments span{width:30px;height:18px}
.screen--desktop .footer__small{font-size:5.6px;line-height:18px}

/* mobile */
.screen--mobile .brand{top:36px;font-size:12px}
.screen--mobile .headline{top:102px}
.screen--mobile .headline__lead{font-size:26px;line-height:1}
.screen--mobile .headline__city{font-size:80px;margin-top:-2px}
.screen--mobile .headline__offer{font-size:17px;margin-left:40px}
.screen--mobile .signup{left:65px;top:251px;width:196px;height:137px;padding:10px 9px}
.screen--mobile .signup__field{height:30px;font-size:10px;padding-left:12px;margin-bottom:8px}
.screen--mobile .signup__button{height:30px;font-size:13px;margin-top:13px}
.screen--mobile .legal{left:70px;width:186px;top:396px;font-size:6.4px;line-height:1.7}
.screen--mobile .quote-badge{left:142px;top:466px;width:41px;height:41px;font-size:30px}
.screen--mobile .section-title{top:527px;font-size:17px}
.screen--mobile .card{top:598px;height:201px}
.screen--mobile .card--main{left:51px;width:224px;padding:60px 12px 0}
.screen--mobile .card--peek-left{left:-200px;width:234px}
.screen--mobile .card--peek-right{left:295px;width:234px}
.screen--mobile .card__avatar{top:-29px;width:68px;height:68px}
.screen--mobile .card__title{font-size:7.6px}
.screen--mobile .card__mark{font-size:38px;margin:6px 0 -8px}
.screen--mobile .card__text{font-size:10px;line-height:1.8}
.screen--mobile .dots{top:817px;gap:10px}
.screen--mobile .dots span{width:7px;height:7px}
.screen--mobile .dots span.is-active{width:11px;height:11px}
.screen--mobile .footer{height:190px;padding-top:11px}
.screen--mobile .footer__links a{font-size:9.5px;line-height:17px}
.screen--mobile .payments{gap:3px;margin:10px 0 14px}
.screen--mobile .payments span{width:36px;height:21px}
.screen--mobile .footer__small{font-size:7.2px;line-height:1.5;padding:0 30px;margin-bottom:10px}
</style>
</head>
<body>

<main class="screen screen--desktop">
  <section class="hero">
    <div class="hero__photo" role="img" aria-label="Photo of a young man walking past the Colosseum in Rome under a pale teal sky, with pine trees on the left"></div>
    <div class="brand"><span class="brand__dot"></span>WANDERLOT</div>
    <h1 class="headline">
      <span class="headline__lead">Win a trip to</span>
      <span class="headline__city">ROME</span>
      <span class="headline__offer">Flights + Hotel <span class="stars">★★★★</span></span>
    </h1>
    <form class="signup">
      <div class="signup__field">Name</div>
      <div class="signup__field">Your Email</div>
      <div class="signup__button">JOIN NOW</div>
    </form>
    <p class="legal">*By entering your email address, you agree to receive updates about the competition and Wanderlot. You can review our competition terms and conditions <u>here</u></p>
  </section>
  <div class="quote-badge">“</div>
  <h2 class="section-title">Recent winners</h2>

  <article class="card" style="left:107px">
    <div class="card__avatar" role="img" aria-label="Winner portrait"></div>
    <p class="card__title">Marta won a four star holiday to the <em>Canary Islands!</em></p>
    <div class="card__mark">“</div>
    <p class="card__text">I wasn't going to be getting a holiday this year, so it's absolutely amazing! I'm so excited !</p>
  </article>
  <article class="card" style="left:306px">
    <div class="card__avatar" role="img" aria-label="Winner portrait"></div>
    <p class="card__title">Priya won a beautiful beach getaway in the <em>Greek Islands!</em></p>
    <div class="card__mark">“</div>
    <p class="card__text">Still can't believe I won! It's a dream that's actually come true! Thank you very much Wanderlot !</p>
  </article>
  <article class="card" style="left:505px">
    <div class="card__avatar" role="img" aria-label="Winner portrait"></div>
    <p class="card__title">Joanne won return flight to the city that never sleeps, <em>New York</em></p>
    <div class="card__mark">“</div>
    <p class="card__text">New York!! I'm so excited! Thanks again - I still can't believe I'll be right there so soon !</p>
  </article>

  <div class="dots"><span class="is-active"></span><span></span><span></span></div>

  <footer class="footer">
    <nav class="footer__links"><a href="#">Terms &amp; Conditions</a><a href="#">Privacy Policy</a></nav>
    <div class="payments" aria-label="Accepted payment cards"><span></span><span></span><span></span><span></span><span></span></div>
    <p class="footer__small">Contact: +44 (0) 20 7946 0123 | Email: hello@wanderlotclub.com</p>
    <p class="footer__small">© 2019 Castelvia Ltd a private limited company registered in England and Wales, Reg No: 00000000. Reg office and postal address: 12 Larkmoor Lane, London, EC1A 4ZZ, UK</p>
  </footer>
</main>

<main class="screen screen--mobile">
  <section class="hero">
    <div class="hero__photo" role="img" aria-label="Photo of a young man walking past the Colosseum in Rome under a pale teal sky"></div>
    <div class="brand"><span class="brand__dot"></span>WANDERLOT</div>
    <h1 class="headline">
      <span class="headline__lead">Win a trip to</span>
      <span class="headline__city">ROME</span>
      <span class="headline__offer">Flights + Hotel <span class="stars">★★★★</span></span>
    </h1>
    <form class="signup">
      <div class="signup__field">Name</div>
      <div class="signup__field">Your Email</div>
      <div class="signup__button">JOIN NOW</div>
    </form>
    <p class="legal">*By entering your email address, you agree to receive updates about the competition and Wanderlot. You can review our competition terms and conditions <u>here</u></p>
  </section>
  <div class="quote-badge">“</div>
  <h2 class="section-title">Recent winners</h2>

  <div class="card card--peek-left"></div>
  <article class="card card--main">
    <div class="card__avatar" role="img" aria-label="Winner portrait"></div>
    <p class="card__title">Marta won a four star holiday to the <em>Canary Islands!</em></p>
    <div class="card__mark">“</div>
    <p class="card__text">I wasn't going to be getting a holiday this year, so it's absolutely amazing! I'm so excited !</p>
  </article>
  <div class="card card--peek-right"></div>

  <div class="dots"><span class="is-active"></span><span></span><span></span><span></span></div>

  <footer class="footer">
    <nav class="footer__links"><a href="#">Terms &amp; Conditions</a><a href="#">Privacy Policy</a></nav>
    <div class="payments" aria-label="Accepted payment cards"><span></span><span></span><span></span><span></span><span></span></div>
    <p class="footer__small">Contact: +44 (0) 20 7946 0123 | Email: hello@wanderlotclub.com</p>
    <p class="footer__small">© 2019 Castelvia Ltd a private limited company registered in England and Wales, Reg No: 00000000. Reg office and postal address: 12 Larkmoor Lane, London, EC1A 4ZZ, UK</p>
  </footer>
</main>

</body>
</html>
```